Professional & attention grabbing.

A business card design, front and back. I already have a logo I will attach, but I am open to something new as well.
Things to include:
Name:
Title:
Phone:
Email:
Wanting something that is professional but attention grabbing.
Also we do a lot of work using drones on natural gas pipelines (leading the future)if you want to include any of that. I'm open to ideas.
Target Market(s)
Natural gas transmission industry / greenhouse gas mitigation industry
Industry/Entity Type
Business
Contact Information for Business Card
All details have been conveyed above.
Colors
Designer to choose colors to be used in the design.
Look and feel
Each slider illustrates characteristics of the customer's brand and the style your logo design should communicate.

```html
<!DOCTYPE html>
<html lang="en">
<head>
<meta charset="utf-8">
<title>Harlow Line Inspections – Business Card</title>
<link href="https://fonts.googleapis.com/css2?family=Roboto+Condensed:wght@400;700&family=Open+Sans:wght@400&display=swap" rel="stylesheet">
<style>
  :root {
    --backdrop: #1c1c1e;
    --card: #ffffff;
    --ink: #353537;
    --red: #c1272d;
    --muted: #4a4a4c;
  }
  html, body {
    margin: 0;
    padding: 0;
    width: 1200px;
    height: 1000px;
    overflow: hidden;
    background: var(--backdrop);
  }
  .canvas {
    position: relative;
    width: 1200px;
    height: 1000px;
  }
  .card {
    position: absolute;
    left: 250px;
    width: 700px;
    height: 400px;
    background: var(--card);
    border-radius: 18px;
    overflow: hidden;
    box-shadow: 0 10px 30px rgba(0,0,0,.45);
  }
  .card--back { top: 70px; }
  .card--front { top: 530px; }

  .brand {
    display: flex;
    align-items: center;
    gap: 14px;
    font-family: "Roboto Condensed", sans-serif;
    font-weight: 700;
    color: var(--ink);
    text-transform: uppercase;
    letter-spacing: 1px;
  }
  .brand__square {
    background: var(--red);
    flex: none;
  }
  .card--back .brand {
    position: absolute;
    left: 0; right: 0; top: 0; bottom: 0;
    justify-content: center;
    font-size: 46px;
  }
  .card--back .brand__square { width: 34px; height: 34px; }

  .card--front .brand {
    position: absolute;
    left: 60px;
    top: 52px;
    font-size: 30px;
  }
  .card--front .brand__square { width: 22px; height: 22px; }

  .person {
    position: absolute;
    left: 60px;
    top: 150px;
    font-family: "Roboto Condensed", sans-serif;
    text-transform: uppercase;
  }
  .person__name {
    margin: 0;
    font-size: 26px;
    font-weight: 700;
    color: var(--red);
    letter-spacing: .5px;
  }
  .person__title {
    margin: 2px 0 0;
    font-size: 17px;
    font-weight: 400;
    color: var(--ink);
  }

  .contact {
    position: absolute;
    right: 50px;
    bottom: 78px;
    margin: 0;
    padding: 0;
    list-style: none;
    font-family: "Open Sans", sans-serif;
    font-size: 17px;
    color: var(--muted);
  }
  .contact__item {
    display: flex;
    align-items: center;
    gap: 10px;
    line-height: 26px;
  }
  .contact__icon { width: 14px; height: 14px; fill: var(--red); flex: none; }

  .footer-band {
    position: absolute;
    left: 0; right: 0; bottom: 0;
    height: 52px;
    background: var(--ink);
  }
  .footer-band__accent {
    position: absolute;
    left: 0; top: 0; bottom: 0;
    width: 46px;
    background: var(--red);
  }
  .footer-band__tile {
    position: absolute;
    left: 46px; top: 0;
    width: 52px; height: 52px;
    background: var(--card);
    display: flex;
    align-items: center;
    justify-content: center;
  }
  .footer-band__tile span {
    width: 22px; height: 22px;
    background: var(--ink);
  }
</style>
</head>
<body>
<main class="canvas">

  <section class="card card--back" aria-label="Card back">
    <div class="brand"><span class="brand__square"></span>Harlow Line Inspections</div>
  </section>

  <section class="card card--front" aria-label="Card front">
    <div class="brand"><span class="brand__square"></span>Harlow Line Inspections</div>

    <div class="person">
      <h1 class="person__name">Daniel Foster</h1>
      <p class="person__title">Founder</p>
    </div>

    <ul class="contact">
      <li class="contact__item">
        <svg class="contact__icon" viewBox="0 0 16 16" aria-hidden="true"><path d="M3 1h3l1.5 4-2 1.3a9 9 0 0 0 4.2 4.2L11 8.5l4 1.5v3a2 2 0 0 1-2 2A12 12 0 0 1 1 3a2 2 0 0 1 2-2z"/></svg>
        000 000 0000
      </li>
      <li class="contact__item">
        <svg class="contact__icon" viewBox="0 0 16 16" aria-hidden="true"><path d="M1 3h14v10H1z M1 3l7 6 7-6" fill="none" stroke="#c1272d" stroke-width="1.6"/></svg>
        info@yourmail.com
      </li>
    </ul>

    <div class="footer-band">
      <div class="footer-band__accent"></div>
      <div class="footer-band__tile"><span></span></div>
    </div>
  </section>

</main>
</body>
</html>
```